Brightpath Wellness Partners

Please design a business card that is colorful but at the same time easy to read. We are based out on Miami Florida. We are a small start up healthcare company that has been in operation for 1 year. Our clients are Hospitals, Insurance companies, and Manage Care health companies. We are growing quickly and lead the niche we are in. Please make the card 2 sided on the front will be the typical info. Logo, Company Name, Persons Name, Title, Cell #, Office #, Fax#, email, website. No address. On the back we will list 5 services that we do. For example Care Transitions, Case management, Risk assessment, Utilization Review.
Target Market(s)
CEO's and COO's of hospitals and healthcare companies.
Industry/Entity Type
Healthcare

```html
<!DOCTYPE html>
<html lang="en">
<head>
<meta charset="utf-8">
<title>Brightpath Wellness Partners – Business Card</title>
<link rel="stylesheet" href="https://fonts.googleapis.com/css2?family=Archivo:ital,wght@0,700;0,800;1,600&family=Open+Sans:wght@400;600&display=swap">
<style>
  :root {
    --navy: #233a8f;
    --royal: #1f6fc0;
    --deep: #2a3a94;
    --red: #e3252b;
    --yellow: #fde02a;
    --pill: #4a8fd4;
    --white: #ffffff;
    --backdrop: #e9e9e9;
    --ink-heading: 'Archivo', Arial, sans-serif;
    --ink-body: 'Open Sans', Arial, sans-serif;
  }
  * { margin: 0; padding: 0; box-sizing: border-box; }
  html, body { width: 1200px; height: 1200px; overflow: hidden; }
  body {
    background: var(--backdrop);
    font-family: var(--ink-body);
    position: relative;
  }
  .card {
    position: absolute;
    left: 120px;
    width: 960px;
    height: 520px;
    background: var(--white);
    box-shadow: 0 6px 18px rgba(0,0,0,0.12);
    overflow: hidden;
  }
  .card--front { top: 50px; }
  .card--back { top: 630px; }

  /* front */
  .front-bands { position: absolute; inset: 0; }
  .brand {
    position: absolute;
    top: 52px;
    left: 250px;
    display: flex;
    align-items: center;
    gap: 22px;
  }
  .brand__dot {
    width: 70px; height: 70px;
    border-radius: 50%;
    background: var(--royal);
  }
  .brand__name {
    font-family: var(--ink-heading);
    font-weight: 800;
    font-size: 34px;
    line-height: 1.05;
    color: var(--navy);
    text-transform: uppercase;
    letter-spacing: 0.5px;
  }
  .person {
    position: absolute;
    left: 70px;
    top: 300px;
    text-transform: uppercase;
  }
  .person__name {
    font-family: var(--ink-body);
    font-weight: 600;
    font-size: 27px;
    color: var(--white);
    letter-spacing: 0.5px;
  }
  .person__title {
    font-family: var(--ink-body);
    font-weight: 600;
    font-size: 22px;
    color: var(--yellow);
    margin-top: 4px;
    margin-left: 30px;
  }
  .divider {
    position: absolute;
    left: 585px;
    top: 300px;
    width: 2px;
    height: 110px;
    background: var(--white);
  }
  .phones {
    position: absolute;
    left: 610px;
    top: 302px;
    list-style: none;
  }
  .phones li {
    display: flex;
    align-items: center;
    gap: 14px;
    color: var(--white);
    font-size: 21px;
    letter-spacing: 1.5px;
    height: 36px;
  }
  .phones svg { width: 18px; height: 18px; fill: var(--yellow); }
  .pill {
    position: absolute;
    height: 40px;
    border-radius: 6px;
    background: var(--pill);
    color: var(--white);
    display: flex;
    align-items: center;
    gap: 14px;
    padding-left: 18px;
    font-size: 21px;
  }
  .pill svg { width: 22px; height: 22px; fill: none; stroke: var(--white); stroke-width: 2; }
  .pill--email { left: 40px; top: 425px; width: 400px; }
  .pill--web { left: 500px; top: 425px; width: 420px; }

  /* back */
  .services {
    position: absolute;
    left: 90px;
    top: 70px;
  }
  .services__heading {
    font-family: var(--ink-body);
    font-weight: 600;
    font-size: 30px;
    color: var(--navy);
    letter-spacing: 1px;
    margin-bottom: 16px;
    margin-left: 40px;
  }
  .services__list { list-style: none; }
  .services__list li {
    display: flex;
    align-items: center;
    gap: 18px;
    font-family: var(--ink-heading);
    font-style: italic;
    font-weight: 600;
    font-size: 24px;
    color: var(--navy);
    height: 44px;
  }
  .services__list li::before {
    content: "";
    width: 14px; height: 14px;
    background: var(--red);
    flex: none;
  }
  .back-brand {
    position: absolute;
    left: 560px;
    top: 150px;
    width: 330px;
    display: flex;
    flex-direction: column;
    align-items: center;
    gap: 24px;
    text-align: center;
  }
  .back-brand__dot {
    width: 110px; height: 110px;
    border-radius: 50%;
    background: var(--royal);
  }
  .back-brand__name {
    font-family: var(--ink-heading);
    font-weight: 800;
    font-size: 30px;
    line-height: 1.1;
    color: var(--navy);
    text-transform: uppercase;
  }
</style>
</head>
<body>

<section class="card card--front" aria-label="Business card front">
  <svg class="front-bands" viewBox="0 0 960 520" preserveAspectRatio="none" aria-hidden="true">
    <defs>
      <linearGradient id="bodyBlue" x1="0" y1="0" x2="0" y2="1">
        <stop offset="0" stop-color="#1f74c4"/>
        <stop offset="1" stop-color="#2c3592"/>
      </linearGradient>
    </defs>
    <path d="M0,130 C200,150 380,250 600,250 C760,250 880,215 960,205 L960,520 L0,520 Z" fill="var(--red)"/>
    <path d="M0,160 C220,190 400,275 620,278 C780,280 890,245 960,238 L960,520 L0,520 Z" fill="var(--yellow)"/>
    <path d="M0,190 C240,230 420,300 640,303 C800,305 900,275 960,270 L960,520 L0,520 Z" fill="url(#bodyBlue)"/>
  </svg>

  <div class="brand">
    <span class="brand__dot"></span>
    <h1 class="brand__name">Brightpath Wellness<br>Partners</h1>
  </div>

  <div class="person">
    <p class="person__name">Persons Name Heare</p>
    <p class="person__title">Your Title Here</p>
  </div>

  <span class="divider"></span>

  <ul class="phones">
    <li>
      <svg viewBox="0 0 24 24" aria-label="Cell"><rect x="6" y="1" width="12" height="22" rx="2"/><rect x="8" y="4" width="8" height="13" fill="#2a5fb0"/></svg>
      305-555-0147
    </li>
    <li>
      <svg viewBox="0 0 24 24" aria-label="Office"><path d="M2 9c0-3 20-3 20 0v2h-5V9H7v2H2z"/><path d="M6 12h12l3 9H3z"/></svg>
      305-555-0182
    </li>
    <li>
      <svg viewBox="0 0 24 24" aria-label="Fax"><rect x="6" y="2" width="12" height="7"/><rect x="2" y="9" width="20" height="10" rx="2"/><rect x="6" y="15" width="12" height="7"/></svg>
      305-555-0199
    </li>
  </ul>

  <div class="pill pill--email">
    <svg viewBox="0 0 24 24" aria-label="Email"><rect x="2" y="5" width="20" height="14"/><path d="M2 5l10 8 10-8"/></svg>
    hello@brightpathwellness.co
  </div>

  <div class="pill pill--web">
    <svg viewBox="0 0 24 24" aria-label="Website"><circle cx="12" cy="12" r="10"/><ellipse cx="12" cy="12" rx="4.5" ry="10"/><path d="M2 12h20"/></svg>
    www.brightpathwellness.co
  </div>
</section>

<section class="card card--back" aria-label="Business card back">
  <div class="services">
    <h2 class="services__heading">WE PROVIDE</h2>
    <ul class="services__list">
      <li>Care Transitions</li>
      <li>Case management</li>
      <li>Risk assessment</li>
      <li>Utilization Review</li>
      <li>Care Transitions</li>
    </ul>
  </div>

  <div class="back-brand">
    <span class="back-brand__dot"></span>
    <p class="back-brand__name">Brightpath Wellness Partners</p>
  </div>
</section>

</body>
</html>
```